Broschüre für Konzepte rund um Immobilien
Zielgruppe
Wir sind ein junges, dynamisches Team und unterstützen Kunden mit individuellen, abgestimmten Konzepten rund um Ihre Immobilie - daher suchen wir ein hochwertiges Design, unsere Zielgruppe liegt Wert auf was neues, nicht das was jeder hat.
Aufgabenstellung
Die Farben und das Layout sollen von der Homepage übernommen werden www.k7-zelt.de..
Den Text entnehmen Sie der angehängten Datei. Bilder, Anordnungen und sonstiges überlasse ich Ihren kreativen Geist! DIN A5 Querformat - Bilder und Texte müssen in einer sehr hohen Auflösung umsetzbar sein!

```html
<!DOCTYPE html>
<html lang="de">
<head>
<meta charset="utf-8">
<title>K7ZELT – Broschüre Titelseite</title>
<link rel="stylesheet" href="https://fonts.googleapis.com/css2?family=Open+Sans:wght@400;600;700&display=swap">
<style>
  :root {
    --page-bg: #e9eaec;
    --paper: #ffffff;
    --navy: #1d2836;
    --navy-soft: #2a3646;
    --text-light: #ffffff;
    --text-muted: #c9ced6;
    --photo-wall: #4f7f9a;
    --photo-window: #dfe3df;
  }
  * { box-sizing: border-box; margin: 0; padding: 0; }
  html, body {
    width: 1200px;
    height: 800px;
    overflow: hidden;
    background: var(--page-bg);
    font-family: "Open Sans", Arial, sans-serif;
  }
  .cover {
    position: absolute;
    left: 40px;
    top: 36px;
    width: 1120px;
    height: 728px;
    background: var(--paper);
    overflow: hidden;
  }
  .cover-photo {
    position: absolute;
    left: 0; top: 0;
    width: 100%;
    height: 370px;
    background: linear-gradient(90deg, var(--photo-wall) 0%, #5d8ca5 42%, #9fb0b5 58%, var(--photo-window) 78%, #eceee9 100%);
  }
  .photo-divider {
    position: absolute;
    left: 0; top: 340px;
    width: 100%;
    height: 60px;
  }
  .title-band {
    position: absolute;
    left: 0; top: 388px;
    width: 100%;
    height: 262px;
    background: linear-gradient(100deg, var(--navy) 0%, var(--navy-soft) 55%, var(--navy) 100%);
  }
  .brand {
    position: absolute;
    left: 60px;
    top: 86px;
    width: 280px;
    color: var(--text-muted);
    text-align: center;
  }
  .brand-mark {
    display: flex;
    align-items: center;
    justify-content: center;
    gap: 12px;
  }
  .brand-dot {
    width: 18px; height: 18px;
    border-radius: 50%;
    background: var(--text-muted);
  }
  .brand-name {
    font-size: 40px;
    font-weight: 600;
    letter-spacing: 1px;
    color: var(--text-muted);
  }
  .brand-tagline {
    margin-top: 6px;
    font-size: 11px;
    font-weight: 600;
    letter-spacing: 0.5px;
  }
  .headline-block {
    position: absolute;
    left: 368px;
    top: 96px;
    width: 660px;
    color: var(--text-light);
  }
  .headline {
    font-size: 27px;
    font-weight: 700;
    letter-spacing: 4px;
    white-space: nowrap;
  }
  .headline-rule {
    margin: 12px 0 10px;
    height: 1px;
    background: var(--text-light);
    opacity: 0.8;
  }
  .subline {
    font-size: 19px;
    font-weight: 400;
    letter-spacing: 0.5px;
  }
</style>
</head>
<body>
  <main class="cover">
    <div class="cover-photo" role="img" aria-label="Foto: Frau sitzt mit einer Tasse auf der Fensterbank vor einem großen Sprossenfenster in einer Wohnung"></div>
    <svg class="photo-divider" viewBox="0 0 1120 60" preserveAspectRatio="none" aria-hidden="true">
      <path d="M0 36 Q560 18 1120 30 L1120 60 L0 60 Z" fill="#1d2836"/>
      <path d="M0 30 Q560 12 1120 24" stroke="#ffffff" stroke-width="7" fill="none"/>
    </svg>
    <section class="title-band">
      <div class="brand">
        <div class="brand-mark">
          <span class="brand-dot"></span>
          <span class="brand-name">K7ZELT</span>
        </div>
        <div class="brand-tagline">BERATEN-BETREUEN-BEGLEITEN</div>
      </div>
      <div class="headline-block">
        <h1 class="headline">BERATEN • BETREUEN • BEGLEITEN</h1>
        <div class="headline-rule"></div>
        <p class="subline">Kompetenz und Know-How im Wohnungsbau</p>
      </div>
    </section>
  </main>
</body>
</html>
```